Powerpoint visual improvements

I need a cover page, and our beliefs page and differentiating factors page / graphic design for our presentation. For the cover page I would just like an attractive design that incorporate our architectural concept with columns and potentially our logo. For the beliefs page I just want a more attractive presentatoin of the concepts. For the differentiating factors page I want a graphic that captures the points about how we are different from competitors. I have used the attached content to date, but I think it can be improved. The text is included in the graphic and I would also like to make sure the firm logo is incorporated.

Target Market(s)

Individual and institutional investors.

Industry/Entity Type

Investment Advisory

Requirements
Must have
• Our corporate colors are generally RGB 145,148,149; 66,68,76; 0,0,153; and 0,63,127. Our logo is attached. Our primary font is Georgia. Our website is www.VorlineCP.com. The key pages are www.VorlineCP.com/beliefs and www.VorlineCP.com/value we are trying to capture in a presentation. We also need a new presentation cover. Use the website as a reference for the type of imagery we like.

```html
<!DOCTYPE html>
<html lang="en">
<head>
<meta charset="utf-8">
<title>Vorline Capital Partners — Presentation Slides</title>
<link href="https://fonts.googleapis.com/css2?family=Gelasio:wght@400;700&display=swap" rel="stylesheet">
<style>
  :root {
    --stage: #e9ebed;
    --marble-light: #f4f5f6;
    --marble-mid: #dfe2e5;
    --marble-shade: #c9cdd1;
    --brand-blue: #0b3f8c;
    --title-blue: #1e5aa0;
    --ink: #2b2d33;
    --white: #ffffff;
    --navy-1: #0c2246;
    --navy-2: #0f3a73;
    --blue-3: #1c4f95;
    --blue-4: #1f64b0;
    --blue-5: #1487cf;
    --blue-6: #1a96d6;
  }
  * { margin: 0; padding: 0; box-sizing: border-box; }
  html, body {
    width: 1200px; height: 675px; overflow: hidden;
    background: var(--stage);
    font-family: "Gelasio", Georgia, serif;
  }
  .canvas { position: relative; width: 1200px; height: 675px; }
  .slide { position: absolute; overflow: hidden; }
  .slide--cover { left: 18px; top: 22px; width: 594px; height: 335px; }
  .slide--factors { left: 590px; top: 316px; width: 591px; height: 332px; background: var(--marble-light); }

  .photo { position: absolute; inset: 0; }
  .photo--columns {
    background:
      linear-gradient(90deg, rgba(255,255,255,0.25), rgba(0,0,0,0) 40%, rgba(255,255,255,0.3) 70%, rgba(0,0,0,0.05)),
      linear-gradient(180deg, var(--marble-mid) 0%, var(--marble-light) 45%, var(--marble-shade) 100%);
  }
  .photo--strip {
    bottom: auto; height: 90px;
    background: linear-gradient(90deg, var(--marble-shade), var(--marble-light) 55%, var(--marble-mid));
  }
  .photo--faded {
    top: 90px;
    background: linear-gradient(180deg, #f7f8f9, #eceef0 60%, #f3f4f5);
  }

  .band { position: absolute; left: 0; width: 100%; height: 100%; }
  .wordmark {
    position: absolute; display: flex; align-items: center; gap: 6px; color: var(--white);
  }
  .wordmark__dot { width: 38px; height: 38px; border-radius: 50%; background: var(--white); }
  .wordmark__name { font-size: 20px; line-height: 1; font-weight: 400; }
  .wordmark__sub { display: block; font-size: 5.5px; letter-spacing: 0.2px; margin-top: 3px; text-transform: uppercase; }

  .slide--cover .wordmark { left: 83px; top: 154px; }
  .tagline { position: absolute; left: 90px; top: 208px; font-size: 12.5px; color: var(--ink); }

  .slide--factors .wordmark { left: 93px; top: 30px; }
  .slide-title {
    position: absolute; left: 392px; top: 20px; font-size: 28px; line-height: 1.2;
    font-weight: 400; color: var(--title-blue);
  }
  .factors { position: absolute; left: 0; top: 0; width: 591px; height: 332px; }
  .factors text { font-family: "Gelasio", Georgia, serif; }
  .factor-label { font-size: 12px; font-weight: 700; fill: var(--white); }
  .factor-num { font-size: 20px; font-weight: 700; fill: var(--white); }
</style>
</head>
<body>
<main class="canvas">

  <section class="slide slide--cover">
    <div class="photo photo--columns" role="img" aria-label="Photograph of white marble column bases"></div>
    <svg class="band" viewBox="0 0 594 335" aria-hidden="true">
      <polygon points="0,139 294,139 242,209 0,209" fill="var(--brand-blue)"/>
    </svg>
    <div class="wordmark">
      <span class="wordmark__dot"></span>
      <span class="wordmark__name">Vorline<span class="wordmark__sub">Capital Partners</span></span>
    </div>
    <p class="tagline">An investment advisor founded by investors.</p>
  </section>

  <section class="slide slide--factors">
    <div class="photo photo--strip" role="img" aria-label="Photograph of marble columns"></div>
    <div class="photo photo--faded" role="img" aria-label="Faded photograph of marble column bases"></div>
    <svg class="band" viewBox="0 0 591 332" aria-hidden="true">
      <polygon points="0,14 303,14 251,84 0,84" fill="var(--brand-blue)"/>
    </svg>
    <div class="wordmark">
      <span class="wordmark__dot"></span>
      <span class="wordmark__name">Vorline<span class="wordmark__sub">Capital Partners</span></span>
    </div>
    <h1 class="slide-title">Differentiating<br>factors</h1>

    <svg class="factors" viewBox="0 0 591 332" role="list" aria-label="Differentiating factors">
      <!-- 01 -->
      <g role="listitem">
        <polygon points="150,121 328,121 300,158 150,158" fill="var(--navy-1)"/>
        <circle cx="150" cy="142" r="23" fill="var(--navy-1)" stroke="var(--white)" stroke-width="3"/>
        <text class="factor-num" x="150" y="149" text-anchor="middle">01</text>
        <text class="factor-label" x="193" y="134">Experienced</text>
        <text class="factor-label" x="193" y="148">Investors</text>
      </g>
      <!-- 02 -->
      <g role="listitem">
        <polygon points="328,134 474,134 474,170 300,170" fill="var(--navy-2)"/>
        <circle cx="473" cy="153" r="23" fill="var(--navy-2)" stroke="var(--white)" stroke-width="3"/>
        <text class="factor-num" x="473" y="160" text-anchor="middle">02</text>
        <text class="factor-label" x="440" y="147" text-anchor="end">Proactive Total Fee</text>
        <text class="factor-label" x="440" y="161" text-anchor="end">Management</text>
      </g>
      <!-- 04 -->
      <g role="listitem">
        <polygon points="83,190 260,190 288,228 83,228" fill="var(--blue-4)"/>
        <circle cx="83" cy="210" r="23" fill="var(--blue-4)" stroke="var(--white)" stroke-width="3"/>
        <text class="factor-num" x="83" y="217" text-anchor="middle">04</text>
        <text class="factor-label" x="115" y="206">Transparent</text>
        <text class="factor-label" x="115" y="220">Communication</text>
      </g>
      <!-- 03 -->
      <g role="listitem">
        <polygon points="242,174 435,174 408,211 242,211" fill="var(--blue-3)"/>
        <circle cx="242" cy="196" r="23" fill="var(--blue-3)" stroke="var(--white)" stroke-width="3"/>
        <text class="factor-num" x="242" y="203" text-anchor="middle">03</text>
        <text class="factor-label" x="276" y="189">Sound Operational</text>
        <text class="factor-label" x="276" y="203">Platform</text>
      </g>
      <!-- 06 -->
      <g role="listitem">
        <polygon points="296,219 490,219 490,257 324,257" fill="var(--blue-6)"/>
        <circle cx="490" cy="242" r="23" fill="var(--blue-6)" stroke="var(--white)" stroke-width="3"/>
        <text class="factor-num" x="490" y="249" text-anchor="middle">06</text>
        <text class="factor-label" x="346" y="236">Institutional</text>
        <text class="factor-label" x="346" y="250">Research Process</text>
      </g>
      <!-- 05 -->
      <g role="listitem">
        <polygon points="101,236 303,236 303,273 128,273" fill="var(--blue-5)"/>
        <circle cx="303" cy="257" r="23" fill="var(--blue-5)" stroke="var(--white)" stroke-width="3"/>
        <text class="factor-num" x="303" y="264" text-anchor="middle">05</text>
        <text class="factor-label" x="267" y="252" text-anchor="end">Independent</text>
        <text class="factor-label" x="267" y="266" text-anchor="end">Portfolio Construction</text>
      </g>
    </svg>
  </section>

</main>
</body>
</html>
```